African homeware retailer needs a web page design

We need a web page design for a new homeware and accessories store based in Johannesburg, South Africa. Our store carries modern African inspired items from designers that support social development and poverty alleviation initiatives. We have a particular preference for outfits that are centred on the empowerment of women.

Our business celebrates the skill, design and product of African craft and the work of designers looking to take that forward in a socially beneficial way (creating employment, developing skills, supporting local crafts people etc). We aim to carry items and inspirations from all over the African continent.

We would like to see a design that communicates African beauty and elegance without the typical tribal references that are made in reference to African craft or art.

We would like the web page to be stylish, uncomplicated, modern, captivating and appealing to the discerning customer. A similar value proposition is that of http://www.lanterwickhouse.example/.

This is an e-commerce website which must be attractive to both individual buyers and design professionals so the website needs to look professional.

Here are links to some websites we like:
http://www.corvellinteriors.example/
http://www.tmerrow.example/

Our logo is attached to the brief.

Target Market(s)

Our target market is female, age 20-50. However should not alienate the design conscious male customer therefore

Industry/Entity Type

E-Commerce

Requirements
Must have
• - A featured product banner which includes a photograph and text. This should be easy to edit as we will be changing the featured product regularly
- An easily expendable products section with categories. Examples of categories could be cushions, bedding, crockery etc. Should be easy to add new categories as well as new product pictures
- Home/landing page should be uncluttered
- Should use the logo and should be easy to change the logo which we have in various colour combinations. We plan to change the logo colours depending on circumstance e.g. make it red and white around Valentines day (similar to the way Quorbit frequently changes the logo on their landing page)

```html
<!DOCTYPE html>
<html lang="en">
<head>
<meta charset="utf-8">
<title>Amani Living — homeware &amp; accessories</title>
<link href="https://fonts.googleapis.com/css2?family=Ubuntu:wght@300;400;500;700&family=Cinzel:wght@700&family=Lora:ital,wght@0,400;1,700&display=swap" rel="stylesheet">
<style>
:root{
  --green:#2c9a3c;
  --green-dark:#1f7a2c;
  --navy:#1b4d69;
  --navy-deep:#163f57;
  --mint:#eef9f7;
  --ink:#222;
  --muted:#555;
  --white:#fff;
}
*{box-sizing:border-box;margin:0;padding:0}
html,body{width:899px;height:1200px;overflow:hidden}
body{font-family:"Ubuntu",sans-serif;color:var(--ink);background:var(--white);position:relative}
.page{position:relative;width:899px;height:1200px;overflow:hidden}
.abs{position:absolute}

/* header */
.header{left:0;top:0;width:899px;height:123px;background:var(--mint);border-top:3px solid var(--green)}
.brand{left:130px;top:22px;display:flex;align-items:center;gap:14px}
.brand-mark{width:62px;height:62px;background:var(--green)}
.brand-name{font-family:"Ubuntu",sans-serif;font-weight:500;font-size:34px;color:var(--green);letter-spacing:3px;line-height:1}
.brand-tag{left:262px;top:90px;font-family:"Lora",serif;font-size:10px;color:var(--navy);letter-spacing:1px}
.account{left:587px;top:32px;font-size:11px;color:var(--navy)}
.cart{left:674px;top:28px;font-size:11px;color:var(--green);display:flex;align-items:center;gap:6px}
.phone{left:667px;top:60px;font-size:15px;font-weight:700;color:var(--green);display:flex;align-items:center;gap:6px}
.search{left:624px;top:87px;width:147px;height:18px;background:#fff;border:1px solid #cfd8d8;font-size:9px;color:#aaa;padding:3px 6px}
.search svg{position:absolute;right:4px;top:3px}

/* nav */
.nav{left:0;top:123px;width:899px;height:32px;background:var(--navy);display:flex;justify-content:center}
.nav ul{list-style:none;display:flex;align-items:center}
.nav li{font-size:11px;color:#fff;padding:0 21px;border-right:1px solid #3f6d85;line-height:18px}
.nav li:last-child{border-right:0}

/* hero */
.hero-bg{left:0;top:155px;width:899px;height:297px;background:linear-gradient(90deg,#e8e4df 0%,#d9d2cb 35%,#c9bdb2 60%,#d7c3b0 80%,#c86a4e 100%)}
.hero-title{left:151px;top:170px;font-family:"Cinzel",serif;font-weight:700;font-size:34px;line-height:39px;color:#111;white-space:nowrap}
.hero-title .blue{color:var(--navy)}
.hero-title .grn{color:var(--green)}
.hero-copy{left:151px;top:331px;width:240px;font-size:10.5px;line-height:16px;color:var(--navy)}
.btn-dark{left:151px;top:373px;width:156px;height:31px;background:var(--navy-deep);color:#fff;font-size:12px;font-weight:700;display:flex;align-items:center;justify-content:center;border:2px solid var(--green);border-radius:2px}
.dots{left:153px;top:417px;display:flex;gap:8px}
.dots span{width:10px;height:10px;border-radius:50%;background:#e8e8e8}
.dots span.on{background:var(--navy);border:2px solid #fff}
.hero-art{left:0;top:90px}

/* intro */
.intro{left:0;top:452px;width:899px;height:160px;background:var(--mint)}
.intro h2{position:absolute;left:0;top:27px;width:899px;text-align:center;font-size:19px;font-weight:700;color:#222;margin-left:-16px}
.intro p{position:absolute;left:145px;top:58px;width:495px;font-size:8.6px;line-height:13.6px;color:#444}
.btn-green{left:653px;top:517px;width:91px;height:31px;background:linear-gradient(#2fa540,#1e7d2c);color:#fff;font-size:12px;font-weight:700;display:flex;align-items:center;justify-content:center;border-radius:2px}

/* sidebar */
.sidebar{left:128px;top:634px;width:172px;height:343px;background:var(--navy);color:#fff}
.sidebar h3{font-size:15px;font-weight:500;margin:15px 0 0 12px}
.cat-list{list-style:none;margin:22px 6px 0 8px}
.cat-list li{font-size:9px;padding:4.5px 0 4.5px 12px;border-bottom:1px solid #346985;position:relative;line-height:10px}
.cat-list li::before{content:"";position:absolute;left:2px;top:7px;border:3px solid transparent;border-left-color:#fff}
.ship{text-align:center;margin-top:26px}
.ship h4{font-size:15px;font-weight:500}
.ship .big{font-size:12px;font-weight:500;margin-top:18px}
.ship .small{font-size:9px;margin-top:4px;color:#dfe9ee}

/* product cards */
.card{width:140px;height:107px;background:#fff;border-radius:3px;overflow:hidden;box-shadow:0 1px 2px rgba(0,0,0,.25)}
.card-title{height:17px;background:var(--green);color:#fff;font-size:9px;font-weight:700;padding:3px 0 0 19px;position:relative}
.card-title::before{content:"";position:absolute;left:7px;top:5px;width:7px;height:7px;border:2px dotted #e7f07a;border-radius:50%}
.card-photo{height:90px}
.card-foot{position:absolute;left:0;bottom:0;width:140px;height:34px}
.detail{position:absolute;right:6px;bottom:4px;font-size:9px;font-weight:700;color:#fff}

/* footer */
.footer{left:0;top:1000px;width:899px;height:200px;background:var(--navy);color:#fff}
.footer h5{position:absolute;font-size:12.5px;font-weight:500}
.quote{left:130px;top:1052px;width:235px;height:75px;background:#f1f1f1;border-radius:9px;color:#444;font-family:"Lora",serif;font-size:8.5px;line-height:11px;padding:18px 18px 0 18px}
.quote-tail{left:305px;top:1124px}
.avatar{left:146px;top:1137px;width:33px;height:33px;border-radius:50%;background:linear-gradient(#b9c2c8,#6b7780);border:2px solid #fff}
.author{left:191px;top:1140px;font-family:"Lora",serif;font-size:10px;line-height:13px;color:#fff}
.author b{font-style:italic}
.contact{left:401px;top:1049px;font-size:10.5px;line-height:13px;color:#fff}
.contact div{display:flex;gap:8px;margin-bottom:8px;align-items:flex-start}
.contact svg{flex:none;margin-top:1px}
.cards{left:401px;top:1154px;display:flex;gap:5px}
.cards span{width:26px;height:16px;background:#e9eef2;border-radius:2px}
.news-copy{left:604px;top:1048px;width:160px;font-size:9px;line-height:11px;color:#fff}
.email{left:605px;top:1075px;width:162px;height:21px;background:#fff;color:#888;font-size:9px;padding:5px 5px}
.social{left:605px;top:1110px;display:flex;gap:7px}
.social span{width:16px;height:16px;background:var(--green);border-radius:2px}
.btn-sub{left:703px;top:1107px;width:65px;height:21px;background:var(--green);border:1px solid #7fd08b;font-size:11px;color:#fff;display:flex;align-items:center;justify-content:center}
.copy{left:614px;top:1160px;font-size:9px;color:#dde8ee}
</style>
</head>
<body>
<div class="page">

  <header class="header abs">
    <div class="brand abs">
      <span class="brand-mark" aria-hidden="true"></span>
      <span class="brand-name">AMANI LIVING</span>
    </div>
    <div class="brand-tag abs">homeware &amp; accessories</div>
    <div class="account abs">Login | Register</div>
    <div class="cart abs">
      <svg width="20" height="16" viewBox="0 0 20 16" aria-hidden="true"><path d="M1 2h3l2 9h10l2-7H5" fill="none" stroke="#2c9a3c" stroke-width="1.6"/><circle cx="8" cy="14" r="1.5" fill="#2c9a3c"/><circle cx="15" cy="14" r="1.5" fill="#2c9a3c"/></svg>
      Cart (0 item) <span style="color:var(--navy)">▾</span>
    </div>
    <div class="phone abs">
      <svg width="15" height="15" viewBox="0 0 16 16" aria-hidden="true"><circle cx="8" cy="8" r="7" fill="none" stroke="#163f57" stroke-width="1.6"/><path d="M8 4v4l3 2" fill="none" stroke="#163f57" stroke-width="1.6"/></svg>
      21 40 55 018
    </div>
    <div class="search abs">Search
      <svg width="11" height="11" viewBox="0 0 12 12" aria-hidden="true"><circle cx="5" cy="5" r="3.8" fill="none" stroke="#222" stroke-width="1.5"/><path d="M8 8l3 3" stroke="#222" stroke-width="1.6"/></svg>
    </div>
  </header>

  <div class="hero-bg abs" role="img" aria-label="Softly blurred interior of a homeware shop with shelves of craft goods"></div>

  <svg class="hero-art abs" width="899" height="380" viewBox="0 90 899 380">
    <defs>
      <linearGradient id="galleryTones" x1="0" y1="0" x2="1" y2="1">
        <stop offset="0" stop-color="#5a3a2a"/><stop offset=".5" stop-color="#8a5a3a"/><stop offset="1" stop-color="#c89a60"/>
      </linearGradient>
      <linearGradient id="lampTones" x1="0" y1="0" x2="0" y2="1">
        <stop offset="0" stop-color="#c9a640"/><stop offset=".55" stop-color="#6d5a2a"/><stop offset="1" stop-color="#a88a4a"/>
      </linearGradient>
    </defs>
    <polygon role="img" aria-label="Photo of a customer browsing framed African art and woven baskets" points="610,95 792,275 610,462 470,322 470,230" fill="url(#galleryTones)" stroke="#fff" stroke-width="3"/>
    <rect role="img" aria-label="Photo of a brass table lamp with a printed fabric shade" x="413" y="160" width="140" height="295" fill="url(#lampTones)"/>
  </svg>

  <nav class="nav abs">
    <ul>
      <li>Home</li><li>About Us</li><li>Services</li><li>Products</li><li>FAQ</li><li>Order Tracking</li><li>Contact Us</li>
    </ul>
  </nav>

  <h1 class="hero-title abs"><span class="blue">Exclusive</span><br><span class="grn">Collection</span><br>of Home<br>Accessories</h1>
  <p class="hero-copy abs">Aenean sem velit, aliquet ut feugiat nec, pla cerat quis odio. Curabitur fringilla imperdiet justo</p>
  <div class="btn-dark abs">Click here to view more</div>
  <div class="dots abs"><span class="on"></span><span></span><span></span></div>

  <section class="intro abs">
    <h2>Mauris vitae enim velit. Proin id lorem nec massa auctor</h2>
    <p>Aenean sem velit, aliquet ut feugiat nec, placerat quis odio. Curabitur fringilla imperdiet justo, vel rutrum elit pharetra at. Nam scelerisque dui eros. Pellentesque ac euismod turpis. Cras lacinia dui leo, ac imperdiet risus tincidunt id. Praesent leo urna, interdum sit amet tortor lobortis, tempor facilisis ligula. Aliquam in egestas urna. Curabitur lacinia velit a libero tincidunt interdum. Maecenas aliquet mauris id leo rhoncus, sed eleifend enim feugiat.</p>
  </section>
  <div class="btn-green abs">View more</div>

  <aside class="sidebar abs">
    <h3>Pruduct Catagories</h3>
    <ul class="cat-list">
      <li>Duis interdum neque vitae lorem</li>
      <li>Condimentum imperdiet.</li>
      <li>Fusce congue ultricies purus.</li>
      <li>Sed interdum nisi vestibulum</li>
      <li>Dapibus dignissim Nulla ac tellus</li>
      <li>Lacus bibendum</li>
      <li>DignissimCurabitur dictum</li>
      <li>Eleifend felis eu ornare Nulla</li>
      <li>Integer malesuada blandit tristi</li>
    </ul>
    <div class="ship">
      <h4>Free Shipping</h4>
      <div class="big">Order over $200</div>
      <div class="small">Not Valid for International Order</div>
    </div>
  </aside>

  <div class="card abs" style="left:331px;top:637px"><div class="card-title">Fruit Basket</div><div class="card-photo" role="img" aria-label="Woven basket in grey, yellow and white stripes" style="background:linear-gradient(#a8a8a8,#d8c840)"></div><svg class="card-foot" viewBox="0 0 140 34"><path d="M0 8 Q60 34 140 2 V34 H0Z" fill="#fff"/><path d="M0 14 Q60 38 140 8 V34 H0Z" fill="#1b4d69"/></svg><span class="detail">Detail</span></div>
  <div class="card abs" style="left:479px;top:637px"><div class="card-title">Rinket Box</div><div class="card-photo" role="img" aria-label="Red lacquered box with a tree silhouette" style="background:radial-gradient(#d81a10,#5a0808)"></div><svg class="card-foot" viewBox="0 0 140 34"><path d="M0 8 Q60 34 140 2 V34 H0Z" fill="#fff"/><path d="M0 14 Q60 38 140 8 V34 H0Z" fill="#1b4d69"/></svg><span class="detail">Detail</span></div>
  <div class="card abs" style="left:628px;top:637px"><div class="card-title">Nabo Tray</div><div class="card-photo" role="img" aria-label="Red tray with a vase and candle" style="background:linear-gradient(#f2ecea,#d8b8b8)"></div><svg class="card-foot" viewBox="0 0 140 34"><path d="M0 8 Q60 34 140 2 V34 H0Z" fill="#fff"/><path d="M0 14 Q60 38 140 8 V34 H0Z" fill="#1b4d69"/></svg><span class="detail">Detail</span></div>

  <div class="card abs" style="left:331px;top:753px"><div class="card-title">Fruit Basket</div><div class="card-photo" role="img" aria-label="Patterned fabric cushion in brown and gold" style="background:linear-gradient(135deg,#7a4a1a,#a8701e)"></div><svg class="card-foot" viewBox="0 0 140 34"><path d="M0 8 Q60 34 140 2 V34 H0Z" fill="#fff"/><path d="M0 14 Q60 38 140 8 V34 H0Z" fill="#1b4d69"/></svg><span class="detail">Detail</span></div>
  <div class="card abs" style="left:479px;top:753px"><div class="card-title">Seed Bead</div><div class="card-photo" role="img" aria-label="Beaded necklace hanging over a white lantern" style="background:linear-gradient(#6a6050,#f0f0f0)"></div><svg class="card-foot" viewBox="0 0 140 34"><path d="M0 8 Q60 34 140 2 V34 H0Z" fill="#fff"/><path d="M0 14 Q60 38 140 8 V34 H0Z" fill="#1b4d69"/></svg><span class="detail">Detail</span></div>
  <div class="card abs" style="left:628px;top:753px"><div class="card-title">Nabo Tray</div><div class="card-photo" role="img" aria-label="Round pink and silver drawer knobs" style="background:linear-gradient(#ddd6d6,#c08a98)"></div><svg class="card-foot" viewBox="0 0 140 34"><path d="M0 8 Q60 34 140 2 V34 H0Z" fill="#fff"/><path d="M0 14 Q60 38 140 8 V34 H0Z" fill="#1b4d69"/></svg><span class="detail">Detail</span></div>

  <div class="card abs" style="left:331px;top:869px"><div class="card-title">Fruit Basket</div><div class="card-photo" role="img" aria-label="Mother of pearl shell bangles" style="background:linear-gradient(135deg,#8fc890,#7a6040)"></div><svg class="card-foot" viewBox="0 0 140 34"><path d="M0 8 Q60 34 140 2 V34 H0Z" fill="#fff"/><path d="M0 14 Q60 38 140 8 V34 H0Z" fill="#1b4d69"/></svg><span class="detail">Detail</span></div>
  <div class="card abs" style="left:479px;top:869px"><div class="card-title">Rinket Box</div><div class="card-photo" role="img" aria-label="Woven wire basket in red, blue and yellow" style="background:linear-gradient(#c8402a,#2a6aa0)"></div><svg class="card-foot" viewBox="0 0 140 34"><path d="M0 8 Q60 34 140 2 V34 H0Z" fill="#fff"/><path d="M0 14 Q60 38 140 8 V34 H0Z" fill="#1b4d69"/></svg><span class="detail">Detail</span></div>
  <div class="card abs" style="left:628px;top:869px"><div class="card-title">Gymstone</div><div class="card-photo" role="img" aria-label="Green gemstone bead bracelet" style="background:radial-gradient(#7aa080,#eeeeee)"></div><svg class="card-foot" viewBox="0 0 140 34"><path d="M0 8 Q60 34 140 2 V34 H0Z" fill="#fff"/><path d="M0 14 Q60 38 140 8 V34 H0Z" fill="#1b4d69"/></svg><span class="detail">Detail</span></div>

  <footer class="footer abs">
    <h5 style="left:135px;top:21px">Testimonials</h5>
    <h5 style="left:398px;top:21px">Contact Info</h5>
    <h5 style="left:599px;top:21px">Subscribe Newsletter</h5>
  </footer>

  <div class="quote abs">Curabitur quis vestibulum nulla. Phasellus nisi mauris, fermentum vitae eros in, volutpat sollicitudin erat. Vestibulum consectetur enim ut ultrices hendrerit.</div>
  <svg class="quote-tail abs" width="30" height="24" viewBox="0 0 30 24" aria-hidden="true"><path d="M0 0 H30 Q28 16 4 23 Q14 12 0 0Z" fill="#f1f1f1"/></svg>
  <div class="avatar abs" role="img" aria-label="Customer portrait"></div>
  <div class="author abs"><b>Aliquam egestas</b><br>imperdiet dictum lacus</div>

  <div class="contact abs">
    <div><svg width="11" height="11" viewBox="0 0 12 12"><path d="M1 6L6 1l5 5H9.5v5h-7V6Z" fill="#fff"/></svg><span>Fusce porta leo 345 egestas<br>sagittis. Integer ut ante</span></div>
    <div><svg width="11" height="11" viewBox="0 0 12 12"><path d="M2 1h3l1 3-2 1c1 2 2 3 3 3l1-2 3 1v3c-6 1-10-4-9-9Z" fill="#fff"/></svg><span>210 555 0140</span></div>
    <div><svg width="12" height="11" viewBox="0 0 12 11"><rect x="3" y="0" width="6" height="3" fill="#fff"/><rect x="0" y="3" width="12" height="5" rx="1" fill="#fff"/><rect x="3" y="7" width="6" height="4" fill="#fff"/></svg><span>210 555 0141</span></div>
    <div><svg width="11" height="9" viewBox="0 0 12 9"><rect x=".5" y=".5" width="11" height="8" fill="none" stroke="#fff"/><path d="M.5.5 6 5l5.5-4.5" fill="none" stroke="#fff"/></svg><span>info@amaniliving.example</span></div>
  </div>
  <div class="cards abs" aria-label="Accepted payment cards"><span></span><span></span><span></span><span></span></div>

  <div class="news-copy abs">Enter you email to get our monthly News updates</div>
  <div class="email abs">Enter Email address</div>
  <div class="social abs" aria-label="Social links"><span></span><span></span><span></span><span></span></div>
  <div class="btn-sub abs">Subscribe</div>
  <div class="copy abs">Copyright © 2014 , all rights reserved.</div>

</div>
</body>
</html>
```